Management consultant needs to update look of website

Currently I have a great word press website but it needs an updated look. I have new text for the site in the attached word document. I also have a list of websites whose design, look, and organization i like as a guide for the designer. The final design should be simple, strong, clear, and project the idea that my brand is a powerful authority in this space. Current site = www.brookfernadvisory.com

Target Market(s)

company owners / executives

Industry/Entity Type

Management Consulting

Number of Pages Required

3 page

Font styles to use
Serif

Colors

Designer to choose colors to be used in the design.

Requirements
Must have
• a simple and clear design and message. professional look. easy navigation. responsive to mobile devices. an easily implemented wordpress theme OR squarespace. use of my logo colors. though I am open to changing to a deep navy or charcoal logo image. source file uploaded.
Nice to have
• i like the cover photo and logo watermark on my current homepage. i like the google map with my logo on the current contact page. i like the animation as well. a great blend of the current site and something that is more seamless.

```html
<!DOCTYPE html>
<html lang="en">
<head>
<meta charset="utf-8">
<title>Brookfern Advisory</title>
<link href="https://fonts.googleapis.com/css2?family=Bebas+Neue&family=Montserrat:ital,wght@0,300;0,400;0,500;1,300;1,400&display=swap" rel="stylesheet">
<style>
  :root {
    --page: #f2f2f3;
    --band: #e5e4e7;
    --navy: #3a4a6b;
    --gold: #c9a74a;
    --ink: #4a5266;
    --ghost: #dcdcde;
    --circle: #e4e4e6;
    --white: #ffffff;
    --photo-warm: #9a8876;
    --photo-dark: #4e4a48;
  }
  * { box-sizing: border-box; margin: 0; padding: 0; }
  html, body { width: 1200px; height: 2624px; overflow: hidden; }
  body {
    position: relative;
    background: var(--page);
    font-family: "Montserrat", Arial, sans-serif;
    color: var(--ink);
  }
  .abs { position: absolute; }

  /* header */
  .brand { left: 131px; top: 58px; display: flex; align-items: center; gap: 12px; }
  .brand-mark { width: 44px; height: 44px; border-radius: 50%; background: var(--gold); }
  .brand-name { font-size: 18px; font-weight: 500; color: var(--gold); letter-spacing: 1px; text-transform: uppercase; line-height: 1.1; }
  .menu-toggle { left: 1028px; top: 68px; width: 40px; }
  .menu-toggle span { display: block; height: 3px; background: var(--navy); margin-bottom: 5px; }

  /* hero */
  .hero-circle { left: 271px; top: 62px; width: 664px; height: 664px; border-radius: 50%; background: var(--circle); }
  .hero { left: 133px; top: 140px; width: 934px; height: 493px; overflow: hidden;
    background: linear-gradient(110deg, var(--photo-dark) 0%, var(--photo-warm) 45%, #c9c3bb 80%, #e2e0dc 100%); }
  .hero-title { left: 50px; top: 308px; font-family: "Bebas Neue", "Oswald", sans-serif; font-weight: 400; color: var(--white); line-height: 0.98; }
  .hero-title .l1 { font-size: 44px; display: block; }
  .hero-title .l2 { font-size: 34px; display: block; }
  .btn { display: flex; align-items: center; justify-content: center; width: 175px; height: 30px;
    border-radius: 15px; background: var(--navy); color: var(--white); font-size: 12px; letter-spacing: 1px; text-transform: uppercase; }
  .hero .btn { position: absolute; left: 51px; top: 411px; }
  .slider-dots { left: 444px; top: 465px; display: flex; gap: 4px; }
  .slider-dots i { width: 8px; height: 8px; border-radius: 50%; background: var(--white); }
  .slider-dots i:first-child { background: var(--gold); }

  /* about */
  .about-circle { left: 26px; top: 778px; width: 472px; height: 472px; border-radius: 50%; background: var(--circle); }
  .about-photo { left: 133px; top: 749px; width: 467px; height: 525px;
    background: linear-gradient(150deg, #d8d2cc 0%, #a48c7c 40%, #7a5a48 75%, #5c4436 100%); }
  .ghost-title { font-family: "Bebas Neue", "Oswald", sans-serif; color: var(--ghost); line-height: 1; }
  .about-ghost { left: 595px; top: 740px; font-size: 140px; }
  .about-aside { left: 828px; top: 828px; text-align: left; font-style: italic; font-weight: 300; color: #bfbfc2; }
  .about-aside .s1 { font-size: 15px; display: block; padding-left: 14px; }
  .about-aside .s2 { font-size: 21px; display: block; text-transform: uppercase; letter-spacing: 1px; }
  .about-heading { left: 619px; top: 926px; font-size: 18px; font-weight: 400; letter-spacing: 3.5px; color: var(--gold); text-transform: uppercase; line-height: 1.25; }
  .about-copy { left: 619px; top: 980px; width: 446px; font-size: 12.5px; line-height: 1.3; color: var(--gold); text-align: justify; }
  .about-copy p + p { margin-top: 16px; }
  .about-more { left: 616px; top: 1161px; }

  /* testimonials */
  .band { left: 0; top: 1434px; width: 1200px; height: 464px; background: var(--band); }
  .testi-ghost { left: 133px; top: 1366px; font-size: 140px; opacity: 0.9; }
  .cards { left: 135px; top: 1525px; display: flex; gap: 5px; }
  .card { width: 188px; height: 262px; background: #f7f7f8; border-radius: 3px; padding: 12px 11px 0; text-align: center; }
  .card-mark { width: 40px; height: 40px; border-radius: 50%; border: 2px solid var(--gold); margin: 0 auto 16px; }
  .card p { font-size: 9.4px; font-style: italic; line-height: 1.3; color: var(--gold); text-align: justify; }
  .card .who { text-align: right; margin-top: 6px; font-size: 9.4px; font-style: italic; color: var(--gold); }
  .testi-more { left: 512px; top: 1833px; }

  /* partner row */
  .partners { left: 135px; top: 2008px; display: flex; gap: 5px; }
  .partner { width: 188px; height: 87px; background: #e3e3e5; border-radius: 3px; display: flex; align-items: center; justify-content: center; }
  .partner span { width: 58px; height: 58px; border-radius: 50%; background: var(--gold); opacity: 0.85; }

  /* footer */
  .footer { left: 0; top: 2190px; width: 1200px; height: 434px; background: linear-gradient(180deg, #e4e4e6 0%, #d9d9db 100%); }
  .footer-title { left: 149px; top: 2214px; font-family: "Bebas Neue", "Oswald", sans-serif; font-weight: 400; font-size: 30px; color: var(--navy); letter-spacing: 0.5px; }
  .footer-lead { left: 149px; top: 2254px; width: 930px; font-size: 13px; line-height: 1.3; color: var(--navy); }
  .footer-rule { left: 149px; top: 2312px; width: 930px; height: 1px; background: #cfcfd2; }
  .footer-brand { left: 104px; top: 2330px; width: 260px; text-align: center; }
  .footer-brand .mark { width: 80px; height: 80px; border-radius: 50%; background: var(--gold); margin: 0 auto 10px; }
  .footer-brand .name { font-size: 17px; font-weight: 500; color: var(--gold); text-transform: uppercase; letter-spacing: 0.5px; white-space: nowrap; line-height: 1.2; }
  .footer-brand .tag { font-size: 10px; font-weight: 500; color: var(--gold); letter-spacing: 1.5px; margin-top: 2px; white-space: nowrap; line-height: 1.2; }
  .hang { left: 149px; top: 2490px; font-size: 12px; letter-spacing: 1px; color: var(--navy); text-transform: uppercase; }
  .socials { left: 149px; top: 2518px; display: flex; gap: 5px; }
  .socials span { width: 42px; height: 42px; border-radius: 50%; border: 2px solid var(--navy); }
  .copyright { left: 149px; top: 2586px; font-size: 9.5px; color: var(--navy); }
  .footer-nav { left: 549px; top: 2377px; font-size: 12px; color: var(--navy); list-style: none; }
  .footer-nav li { margin-bottom: 10px; }
  .footer-nav li:first-child { text-transform: uppercase; letter-spacing: 0.5px; margin-bottom: 12px; }
  .signup { left: 829px; top: 2356px; width: 252px; }
  .signup h3 { font-family: "Bebas Neue", "Oswald", sans-serif; font-weight: 400; font-size: 17px; color: var(--navy); letter-spacing: 0.5px; }
  .signup p { font-size: 10px; line-height: 1.3; color: var(--navy); margin: 4px 0 8px; }
  .field { height: 26px; background: var(--white); border-radius: 3px; margin-bottom: 4px; font-size: 10px; letter-spacing: 1.5px; color: var(--navy); padding: 7px 10px; text-transform: uppercase; }
  .signup .btn { margin-top: 8px; }
</style>
</head>
<body>

<header>
  <div class="abs brand"><span class="brand-mark"></span><span class="brand-name">Brookfern<br>Advisory</span></div>
  <div class="abs menu-toggle" aria-label="Menu"><span></span><span></span><span></span></div>
</header>

<div class="abs hero-circle"></div>
<section class="abs hero" role="img" aria-label="Photo of a consultant leading a workshop with a team seated at tables with laptops">
  <h1 class="abs hero-title"><span class="l1">Great Companies Succeed</span><span class="l2">By Investing In The Right People</span></h1>
  <a class="btn">Know More</a>
  <div class="abs slider-dots"><i></i><i></i><i></i><i></i><i></i></div>
</section>

<section class="about">
  <div class="abs about-circle"></div>
  <div class="abs about-photo" role="img" aria-label="Photo of three women reviewing notes and a book at a table"></div>
  <div class="abs ghost-title about-ghost">About</div>
  <div class="abs about-aside"><span class="s1">I Am Brookfern</span><span class="s2">And I'm Here To Help</span></div>
  <h2 class="abs about-heading">Great Companies Succeed<br>By Investing In The Right People</h2>
  <div class="abs about-copy">
    <p>It's no secret that long-term business success requires a smart investment in the right people for your company. And yet, knowing how to cultivate a strong staff and keep them focused on the road ahead can be challenging for even the savviest organizational leaders and human resource executives.</p>
    <p>I'm Dr. Elena Marsh and I want to help business owners, leaders, and HR teams understand how to identify, develop, and retain talented professionals who can take your success to the next level.</p>
  </div>
  <a class="abs btn about-more">Know More</a>
</section>

<section class="testimonials">
  <div class="abs band"></div>
  <div class="abs ghost-title testi-ghost">Testimonials</div>
  <div class="abs cards">
    <article class="card"><div class="card-mark"></div><p>After working in the consulting business for 12 years, I met Elena. I was immediately impressed by her ability to ask the right questions. It is rare to find someone with her credentials who also continues to have deep curiosity and creativity about their area of expertise. Elena has a passion for helping people reach their full potential from the classroom to c-suite and Brookfern Advisory is a powerful platform to push people to their personal best.</p><div class="who">- Clara M</div></article>
    <article class="card"><div class="card-mark"></div><p>After working in the consulting business for 12 years, I met Elena. I was immediately impressed by her ability to ask the right questions. It is rare to find someone with her credentials who also continues to have deep curiosity and creativity about their area of expertise. Elena has a passion for helping people reach their full potential from the classroom to c-suite and Brookfern Advisory is a powerful platform to push people to their personal best.</p><div class="who">- Clara M</div></article>
    <article class="card"><div class="card-mark"></div><p>After working in the consulting business for 12 years, I met Elena. I was immediately impressed by her ability to ask the right questions. It is rare to find someone with her credentials who also continues to have deep curiosity and creativity about their area of expertise. Elena has a passion for helping people reach their full potential from the classroom to c-suite and Brookfern Advisory is a powerful platform to push people to their personal best.</p><div class="who">- Clara M</div></article>
    <article class="card"><div class="card-mark"></div><p>After working in the consulting business for 12 years, I met Elena. I was immediately impressed by her ability to ask the right questions. It is rare to find someone with her credentials who also continues to have deep curiosity and creativity about their area of expertise. Elena has a passion for helping people reach their full potential from the classroom to c-suite and Brookfern Advisory is a powerful platform to push people to their personal best.</p><div class="who">- Clara M</div></article>
    <article class="card"><div class="card-mark"></div><p>After working in the consulting business for 12 years, I met Elena. I was immediately impressed by her ability to ask the right questions. It is rare to find someone with her credentials who also continues to have deep curiosity and creativity about their area of expertise. Elena has a passion for helping people reach their full potential from the classroom to c-suite and Brookfern Advisory is a powerful platform to push people to their personal best.</p><div class="who">- Clara M</div></article>
  </div>
  <a class="abs btn testi-more">More</a>
</section>

<section class="abs partners" aria-label="Partners">
  <div class="partner"><span></span></div>
  <div class="partner"><span></span></div>
  <div class="partner"><span></span></div>
  <div class="partner"><span></span></div>
  <div class="partner"><span></span></div>
</section>

<footer>
  <div class="abs footer"></div>
  <h2 class="abs footer-title">Learn To Inspire Employees And Unlock Their Maximum Potential</h2>
  <p class="abs footer-lead">If you're struggling to connect with today's employees and you need to develop a better way to lead them, I want to help you become the very best leader possible.</p>
  <div class="abs footer-rule"></div>
  <div class="abs footer-brand"><div class="mark"></div><div class="name">Brookfern Advisory</div><div class="tag">Strategy. Workshops. Coaching.</div></div>
  <div class="abs hang">Hang out with us</div>
  <div class="abs socials"><span aria-label="Social link"></span><span aria-label="Social link"></span><span aria-label="Social link"></span><span aria-label="Social link"></span></div>
  <p class="abs copyright">© Copyright 2015, Brookfern Advisory, LLC | All Rights Reserved</p>
  <ul class="abs footer-nav"><li>Company</li><li>Home</li><li>About us</li><li>Services</li><li>Learn more</li></ul>
  <div class="abs signup">
    <h3>Want More Information?</h3>
    <p>Sign-up below to receive news and updates about Brookfern Advisory, our custom programs for college students, and other leadership training opportunities.</p>
    <div class="field">Name</div>
    <div class="field">Email Address</div>
    <a class="btn">Subscribe</a>
  </div>
</footer>

</body>
</html>
```